Brand new leaflet design creative ideas.

I need a flyer designed for my business

I run a pay weekly carpet business and need designs for a flyer this design i will also want to enable it on letterheads business cards and a logo from it when created.

my domain name is www.pallowmere.co.uk / www.pallowmere.com

Our main competitor i have attached his design to this brief to give you a bit of an idea on how we work, however i do not want a copycat design i want a brand new design something not like theres but eye catching direct to the point.

We are open to colour suggestions as long as the colours work.
Thank you.

Target Market(s)

This print material will be delivered to customers houses.

Industry/Entity Type

Flooring

Font styles to use
Serif
Sans Serif

Requirements
Must have
• Website domain name,
• Various print options CMYK, PDF
Nice to have
• Creativity eye catching
Should not have
• SHOULD NOT BE A COPYCAT DESIGN SOMETHING NEW & CREATIVE

```html
<!DOCTYPE html>
<html lang="en">
<head>
<meta charset="utf-8">
<title>Pallowmere – Pay Weekly Carpets Leaflet</title>
<link href="https://fonts.googleapis.com/css2?family=DM+Serif+Display&family=Work+Sans:wght@400;500;700&display=swap" rel="stylesheet">
<style>
  :root {
    --teal-deep: #0f3336;
    --teal: #164a4e;
    --teal-soft: #2c6468;
    --cream: #f5ede0;
    --cream-dark: #e6d9c3;
    --coral: #e5573a;
    --coral-dark: #c4432a;
    --ink: #1d2224;
    --white: #ffffff;
  }
  * { margin: 0; padding: 0; box-sizing: border-box; }
  html, body { width: 950px; height: 1200px; overflow: hidden; background: var(--white); }
  .leaflet {
    position: relative; width: 950px; height: 1200px; overflow: hidden;
    background: var(--teal);
    font-family: "Work Sans", sans-serif; color: var(--cream);
  }
  .keep-line {
    position: absolute; left: 0; top: 0; width: 100%; height: 56px;
    background: var(--cream); color: var(--teal-deep);
    display: flex; align-items: center; justify-content: center;
    font-size: 19px; font-weight: 500; letter-spacing: 2px; text-transform: uppercase;
  }
  .brand {
    position: absolute; left: 60px; top: 84px;
  }
  .brand-name {
    display: flex; align-items: center; gap: 18px;
    font-family: "DM Serif Display", serif; font-size: 88px; line-height: 1; color: var(--cream);
  }
  .brand-name .mark { width: 26px; height: 26px; background: var(--coral); flex: none; }
  .brand-tagline {
    margin-top: 14px; margin-left: 44px;
    font-size: 22px; font-weight: 500; letter-spacing: 3px; text-transform: uppercase; color: var(--coral);
  }
  .hero-copy { position: absolute; left: 60px; top: 290px; width: 410px; }
  .hero-title {
    font-family: "DM Serif Display", serif; font-size: 84px; line-height: 88px; color: var(--white);
  }
  .hero-title em { font-style: normal; color: var(--coral); }
  .hero-text { margin-top: 22px; font-size: 23px; line-height: 33px; color: var(--cream-dark); }
  .offer-card {
    position: absolute; left: 60px; top: 600px; width: 410px; height: 82px;
    background: var(--coral); border-radius: 8px;
    display: flex; flex-direction: column; justify-content: center; padding-left: 26px;
  }
  .offer-card .headline { font-size: 28px; font-weight: 700; letter-spacing: 2px; color: var(--white); text-transform: uppercase; }
  .offer-card .subline { font-size: 19px; font-weight: 500; color: var(--cream); }
  .photo-home {
    position: absolute; left: 510px; top: 282px; width: 380px; height: 400px;
    border-radius: 190px 190px 20px 20px;
    background: linear-gradient(170deg, #f4f1ec 0%, #e4d6c2 55%, #b58f6c 100%);
  }
  .benefits-panel {
    position: absolute; left: 60px; top: 720px; width: 830px; height: 290px;
    background: var(--cream); border-radius: 14px; padding: 30px 40px; color: var(--ink);
  }
  .benefits-title {
    font-family: "DM Serif Display", serif; font-size: 32px; line-height: 38px; color: var(--teal-deep);
    margin-bottom: 16px;
  }
  .benefits { list-style: none; display: grid; grid-template-columns: 1fr 1fr; column-gap: 30px; row-gap: 8px; }
  .benefits li {
    display: flex; align-items: center; gap: 14px;
    font-size: 24px; line-height: 44px; font-weight: 500;
  }
  .benefits svg { width: 28px; height: 28px; flex: none; }
  .call-band {
    position: absolute; left: 0; top: 1036px; width: 100%; height: 104px;
    background: var(--teal-deep);
    display: flex; align-items: center; gap: 28px; padding-left: 60px;
  }
  .call-band svg { width: 52px; height: 52px; flex: none; }
  .call-label { font-size: 20px; font-weight: 500; letter-spacing: 3px; text-transform: uppercase; color: var(--cream-dark); }
  .call-number { font-size: 60px; font-weight: 700; letter-spacing: 2px; color: var(--white); line-height: 1; }
  .web-strip {
    position: absolute; left: 0; top: 1140px; width: 100%; height: 60px;
    background: var(--coral); color: var(--white);
    display: flex; align-items: center; justify-content: space-between; padding: 0 60px;
  }
  .web-address { font-size: 26px; font-weight: 700; letter-spacing: 0.5px; }
  .follow { font-size: 20px; font-weight: 500; display: flex; align-items: center; gap: 10px; }
  .follow .dot { width: 18px; height: 18px; border-radius: 50%; background: var(--white); }
</style>
</head>
<body>
<main class="leaflet">
  <div class="keep-line">Please keep this card safe or pass it on to a friend!</div>

  <header class="brand">
    <div class="brand-name"><span class="mark"></span>Pallowmere</div>
    <div class="brand-tagline">Pay weekly carpets &amp; flooring</div>
  </header>

  <section class="hero-copy">
    <h1 class="hero-title">Spread<br><em>the cost.</em></h1>
    <p class="hero-text">New carpets fitted now, paid for a little each week.</p>
  </section>

  <div class="photo-home" role="img" aria-label="Photo of a child and a white kitten relaxing on a soft new carpet at home"></div>

  <div class="offer-card">
    <span class="headline">Congratulation</span>
    <span class="subline">You've been selected</span>
  </div>

  <section class="benefits-panel">
    <h2 class="benefits-title">Every order includes</h2>
    <ul class="benefits">
      <li><svg viewBox="0 0 28 28"><circle cx="14" cy="14" r="13" fill="#164a4e"/><path d="M8 14.5 L12.5 19 L20 10" stroke="#fff" stroke-width="3" fill="none"/></svg>Interest free credit</li>
      <li><svg viewBox="0 0 28 28"><circle cx="14" cy="14" r="13" fill="#164a4e"/><path d="M8 14.5 L12.5 19 L20 10" stroke="#fff" stroke-width="3" fill="none"/></svg>Pay only £500 per week</li>
      <li><svg viewBox="0 0 28 28"><circle cx="14" cy="14" r="13" fill="#164a4e"/><path d="M8 14.5 L12.5 19 L20 10" stroke="#fff" stroke-width="3" fill="none"/></svg>No credit check</li>
      <li><svg viewBox="0 0 28 28"><circle cx="14" cy="14" r="13" fill="#164a4e"/><path d="M8 14.5 L12.5 19 L20 10" stroke="#fff" stroke-width="3" fill="none"/></svg>Free home measuring</li>
      <li><svg viewBox="0 0 28 28"><circle cx="14" cy="14" r="13" fill="#164a4e"/><path d="M8 14.5 L12.5 19 L20 10" stroke="#fff" stroke-width="3" fill="none"/></svg>Free underlay</li>
      <li><svg viewBox="0 0 28 28"><circle cx="14" cy="14" r="13" fill="#164a4e"/><path d="M8 14.5 L12.5 19 L20 10" stroke="#fff" stroke-width="3" fill="none"/></svg>Free grippers</li>
      <li><svg viewBox="0 0 28 28"><circle cx="14" cy="14" r="13" fill="#164a4e"/><path d="M8 14.5 L12.5 19 L20 10" stroke="#fff" stroke-width="3" fill="none"/></svg>Free door trims</li>
    </ul>
  </section>

  <section class="call-band">
    <svg viewBox="0 0 52 52" aria-hidden="true"><circle cx="26" cy="26" r="25" fill="#e5573a"/><path d="M19 14 C17 14 15 16 15.5 19 C17 28 24 35 33 36.5 C36 37 38 35 38 33 L38 30.5 L32.5 28.5 L30 31 C26 29.5 22.5 26 21 22 L23.5 19.5 L21.5 14 Z" fill="#fff"/></svg>
    <span class="call-label">Call us</span>
    <span class="call-number">0800 555 0142</span>
  </section>

  <footer class="web-strip">
    <span class="web-address">www.pallowmere.com</span>
    <span class="follow">Follow us : Pallowmere <span class="dot"></span></span>
  </footer>
</main>
</body>
</html>
```